Electrician Letterhead Design BLR

We need some letterhead for our bills and other papers.
Customer address is on the right side (Swiss format)
A4 format

Design should also be applicable on Cards

Target Market(s)

Private Customers, Small Business

Industry/Entity Type

Electrician

Other font styles liked:
• incised 901

Colors
00AB8E
00BBA5
67D7C9
C6EFE9
E9F9F6

```html
<!DOCTYPE html>
<html lang="de">
<head>
<meta charset="utf-8">
<title>BLR Letterhead</title>
<link href="https://fonts.googleapis.com/css2?family=Poppins:wght@400;600;700&display=swap" rel="stylesheet">
<style>
  :root {
    --backdrop: #dadada;
    --paper: #ffffff;
    --brand: #0aa08e;
    --ink: #1a1a1a;
  }
  html, body {
    margin: 0;
    padding: 0;
    width: 1200px;
    height: 947px;
    overflow: hidden;
    background: var(--backdrop);
    font-family: "Poppins", sans-serif;
  }
  .letterhead {
    position: absolute;
    left: 364px;
    top: 179px;
    width: 472px;
    height: 605px;
    background: var(--paper);
    overflow: hidden;
  }
  .brand {
    position: absolute;
    top: 18px;
    left: 0;
    width: 100%;
    text-align: center;
  }
  .brand-name {
    display: block;
    font-weight: 700;
    font-size: 50px;
    line-height: 1;
    letter-spacing: 1px;
    color: var(--brand);
  }
  .brand-tagline {
    display: block;
    margin-top: 4px;
    font-weight: 600;
    font-size: 7px;
    letter-spacing: 0.3px;
    color: var(--ink);
  }
  .address-band {
    position: absolute;
    left: 127px;
    top: 550px;
    width: 345px;
    height: 20px;
    background: var(--brand);
    color: var(--paper);
    font-size: 9.5px;
    line-height: 20px;
    text-align: right;
    padding-right: 29px;
    box-sizing: border-box;
  }
  .contact-line {
    position: absolute;
    right: 27px;
    top: 579px;
    font-size: 9.5px;
    line-height: 16px;
    color: var(--ink);
    white-space: nowrap;
  }
  .contact-label {
    color: var(--brand);
    font-weight: 600;
  }
</style>
</head>
<body>
  <main class="letterhead">
    <header class="brand">
      <span class="brand-name">BLR</span>
      <span class="brand-tagline">Elektrotechnik Bauler GmbH</span>
    </header>

    <footer>
      <div class="address-band">Your Address line here, Country Code 0123456</div>
      <p class="contact-line" style="margin:0">
        <span class="contact-label">P:</span> 044-123 456 789 |
        <span class="contact-label">E:</span> info@webname.com |
        <span class="contact-label">W:</span>&nbsp; www.websitename.com
      </p>
    </footer>
  </main>
</body>
</html>
```